Load Up Your Cart

Require two banners with a size of 980 x 450 pixels
Similar natural looking banner as per attachment. The background is supposed to be a cardboard carton
price "$9.95"
Wording and layout the same as attached file

```html
<!DOCTYPE html>
<html lang="en">
<head>
<meta charset="utf-8">
<title>Load Up Your Cart Banner</title>
<link rel="stylesheet" href="https://fonts.googleapis.com/css2?family=Oswald:wght@500;700&family=Bowlby+One&family=Open+Sans&display=swap">
<style>
  :root {
    --page-bg: #ffffff;
    --rule-green: #4f8a2b;
    --title-red: #c0141b;
    --label-ink: #4a4038;
    --stamp-brown: #574535;
    --price-red: #b5121b;
    --tape-light: #e0b88a;
    --tape-mid: #d4a877;
    --tape-dark: #c39463;
    --card-light: #d9be89;
    --card-mid: #cdb07a;
    --card-dark: #c3a46c;
  }
  * { margin: 0; padding: 0; box-sizing: border-box; }
  html, body { width: 1200px; height: 905px; overflow: hidden; background: var(--page-bg); }
  .sheet { position: relative; width: 1200px; height: 905px; font-family: "Open Sans", sans-serif; }
  .sheet-rule { position: absolute; left: 0; width: 1200px; height: 6px; background: var(--rule-green); }
  .sheet-rule--top { top: 0; }
  .sheet-rule--bottom { bottom: 0; }
  .sheet-title { position: absolute; top: 9px; left: 0; width: 1200px; text-align: center; font-size: 16px; color: var(--title-red); }
  .banner-label { position: absolute; left: 59px; font-size: 15px; color: var(--label-ink); }

  .banner { position: absolute; left: 164px; width: 804px; height: 368px; overflow: hidden; box-shadow: 2px 3px 5px rgba(0,0,0,.35); }
  .banner--tape { top: 72px; }
  .banner--plain { top: 491px; }
  .banner-texture { position: absolute; inset: 0; }
  .banner--tape .banner-texture {
    background: linear-gradient(180deg, var(--tape-light) 0%, var(--tape-mid) 28%, var(--tape-dark) 48%, var(--tape-mid) 62%, var(--tape-light) 100%);
  }
  .banner--plain .banner-texture {
    background: linear-gradient(135deg, var(--card-light) 0%, var(--card-mid) 55%, var(--card-dark) 100%);
  }
  .stamp { position: absolute; left: 0; top: 0; width: 804px; height: 368px; }
  .stamp-word { position: absolute; font-family: "Bowlby One", sans-serif; color: var(--stamp-brown); line-height: 1; text-shadow: 3px 3px 0 rgba(87,69,53,.45); }
  .stamp-load { left: 10px; top: 112px; font-size: 92px; letter-spacing: -1px; }
  .stamp-up { left: 10px; top: 219px; font-size: 78px; }
  .stamp-your { left: 160px; top: 212px; font-size: 38px; }
  .stamp-cart { left: 160px; top: 248px; font-size: 38px; }

  .offer { position: absolute; font-family: "Oswald", sans-serif; line-height: 1; transform-origin: left top; white-space: nowrap; }
  .offer-price { left: 346px; top: 24px; font-size: 206px; font-weight: 700; color: var(--price-red); transform: scaleX(.72); }
  .offer-headline { left: 326px; top: 212px; font-size: 86px; font-weight: 700; color: var(--price-red); transform: scaleX(.62); }
  .offer-terms { left: 281px; top: 290px; font-size: 48px; font-weight: 500; color: var(--stamp-brown); transform: scaleX(.67); }
</style>
</head>
<body>
<div class="sheet">
  <div class="sheet-rule sheet-rule--top"></div>
  <h1 class="sheet-title">Load Up Your Cart Banner</h1>

  <p class="banner-label" style="top:244px">Banner C</p>
  <section class="banner banner--tape">
    <div class="banner-texture" role="img" aria-label="Cardboard carton surface with a strip of brown packing tape"></div>
    <svg class="stamp" viewBox="0 0 804 368" aria-hidden="true">
      <circle cx="150" cy="200" r="150" fill="none" stroke="var(--stamp-brown)" stroke-width="4"/>
      <line x1="10" y1="108" x2="292" y2="100" stroke="var(--stamp-brown)" stroke-width="3"/>
      <line x1="10" y1="300" x2="292" y2="292" stroke="var(--stamp-brown)" stroke-width="3"/>
    </svg>
    <span class="stamp-word stamp-load">LOAD</span>
    <span class="stamp-word stamp-up">UP</span>
    <span class="stamp-word stamp-your">YOUR</span>
    <span class="stamp-word stamp-cart">CART</span>
    <p class="offer offer-price">$9.95</p>
    <p class="offer offer-headline">FLAT RATE SHIPPING</p>
    <p class="offer offer-terms">NO MINIMUMS. NO CODES. NO GIMMICKS.</p>
  </section>

  <p class="banner-label" style="top:651px">Banner C</p>
  <section class="banner banner--plain">
    <div class="banner-texture" role="img" aria-label="Corrugated cardboard carton surface"></div>
    <svg class="stamp" viewBox="0 0 804 368" aria-hidden="true">
      <circle cx="150" cy="200" r="150" fill="none" stroke="var(--stamp-brown)" stroke-width="4"/>
      <line x1="10" y1="108" x2="292" y2="100" stroke="var(--stamp-brown)" stroke-width="3"/>
      <line x1="10" y1="300" x2="292" y2="292" stroke="var(--stamp-brown)" stroke-width="3"/>
    </svg>
    <span class="stamp-word stamp-load">LOAD</span>
    <span class="stamp-word stamp-up">UP</span>
    <span class="stamp-word stamp-your">YOUR</span>
    <span class="stamp-word stamp-cart">CART</span>
    <p class="offer offer-price">$9.95</p>
    <p class="offer offer-headline">FLAT RATE SHIPPING</p>
    <p class="offer offer-terms">NO MINIMUMS. NO CODES. NO GIMMICKS.</p>
  </section>

  <div class="sheet-rule sheet-rule--bottom"></div>
</div>
</body>
</html>
```